Billboard Design for Modern Dispensary

Hello!
We need a eye-catching 12' x 24' billboard designed for a very successful, modern cannabis dispensary on the Oregon coast, United States. Because of rules, we cannot have any marijuana leafs or other cannabis related images (flower, joints, smoke, etc). We can use the words "Shop" or "Dispensary" - we cannot use the words "cannabis", "marijuana".

Some ideas we had are 3 words stacked on left or center of billboard - maybe across bottom we have horizontal logo and the following words - “South of bridge in Gull Harbor”
Another idea is to have a small bubble in bottom/top corner with image of our dog (face only) - with some words around it - like "BONUS Shop Dog" or "Cute Shop Dog" or "Best Shop Dog" or "Friendly Staff"

here's some 3 word examples:
ENJOY
YOUR
TRIP

or

FEEL
GOOD
JUST
AHEAD

or

GOOD
VIBES
ONLY

or

GOOD
TIMES
CHILL
VIBES

I have attached our logo. I have also included a stacked logo version (vertical, not horizontal). the formats are .EPS and .PDF - the logos were created in Affinity Design 2.x.

Our website is coralnook.net if you want to see more images, etc about our dispensary.

Artwork Requirements:
The billboard is 12' tall x 25' wide
The artwork needs to be 1”=1’ @ 300dpi
Please add 6” of bleed all around so your total artwork is 13”x26”
Final deliverable should be .Ai file.

Font styles to use
Sans Serif

Colors
0054AA
0677BA
7BADD7
CADEEF
E8F1F8

Requirements
Nice to have
• See the project description - we included some ideas to consider.
Should not have
• No cannabis images, like flower, cannabis leaves, paraphenlia, cartridges, joints, etc.

```html
<!DOCTYPE html>
<html lang="en">
<head>
<meta charset="utf-8">
<title>Good Vibes Only – Coral Nook Billboard</title>
<link rel="stylesheet" href="https://fonts.googleapis.com/css2?family=Montserrat:ital,wght@0,500;0,900;1,900&family=Arimo:wght@700&display=swap">
<style>
  :root {
    --navy-deep: #072640;
    --navy: #0b3553;
    --teal-blob: #12607a;
    --teal-soft: #1c7f93;
    --ring-teal: #1a8c93;
    --sky: #48bff0;
    --sunshine: #ffdc14;
    --ink: #141414;
    --brand-blue: #3d8fd8;
    --white: #ffffff;
    --fur-light: #e9d5b4;
    --fur-dark: #b89a72;
  }
  html, body {
    margin: 0;
    padding: 0;
    width: 1200px;
    height: 600px;
    overflow: hidden;
    background: var(--navy-deep);
  }
  .billboard {
    position: relative;
    width: 1200px;
    height: 600px;
    overflow: hidden;
  }
  .billboard svg { display: block; }
  .headline {
    font-family: "Montserrat", sans-serif;
    font-weight: 900;
    font-style: italic;
  }
  .headline-shadow { fill: var(--ink); }
  .headline-sky { fill: var(--sky); }
  .headline-sun { fill: var(--sunshine); }
  .badge-caption {
    font-family: "Montserrat", sans-serif;
    font-weight: 900;
    font-size: 30px;
    fill: var(--white);
    stroke: var(--ink);
    stroke-width: 2px;
    paint-order: stroke;
    letter-spacing: 1px;
  }
  .brand-name {
    font-family: "Montserrat", sans-serif;
    font-weight: 500;
    font-size: 36px;
    fill: var(--brand-blue);
  }
  .location-line {
    font-family: "Arimo", sans-serif;
    font-weight: 700;
    font-size: 29px;
    fill: var(--white);
  }
</style>
</head>
<body>
<main class="billboard">
  <svg width="1200" height="600" viewBox="0 0 1200 600" xmlns="http://www.w3.org/2000/svg">
    <defs>
      <linearGradient id="bg-gradient" x1="0" y1="0" x2="1" y2="1">
        <stop offset="0" stop-color="var(--navy)"/>
        <stop offset="0.6" stop-color="#0a2f4b"/>
        <stop offset="1" stop-color="var(--navy-deep)"/>
      </linearGradient>
      <radialGradient id="glow" cx="0.62" cy="0.1" r="0.6">
        <stop offset="0" stop-color="#2a86a6" stop-opacity="0.7"/>
        <stop offset="1" stop-color="#2a86a6" stop-opacity="0"/>
      </radialGradient>
      <radialGradient id="dog-tones" cx="0.5" cy="0.45" r="0.6">
        <stop offset="0" stop-color="var(--fur-light)"/>
        <stop offset="1" stop-color="var(--fur-dark)"/>
      </radialGradient>
      <pattern id="stripes" width="26" height="26" patternUnits="userSpaceOnUse" patternTransform="rotate(45)">
        <rect width="2" height="26" fill="#ffffff" opacity="0.05"/>
      </pattern>
      <path id="caption-arc" d="M 756 252 A 160 160 0 0 0 1076 252"/>
    </defs>

    <!-- background -->
    <rect class="backdrop" width="1200" height="600" fill="url(#bg-gradient)"/>
    <rect class="backdrop-glow" width="1200" height="600" fill="url(#glow)"/>
    <path class="backdrop-stripes" d="M 820 0 L 1200 0 L 1200 420 Z" fill="url(#stripes)"/>

    <!-- flowing blobs -->
    <path class="blob blob-top" d="M 500 0 L 770 0 C 790 60 760 120 720 170 C 690 210 700 260 740 300 C 700 320 640 300 610 250 C 580 200 520 190 470 160 C 430 130 450 50 500 0 Z" fill="var(--teal-blob)" opacity="0.55"/>
    <path class="blob blob-left" d="M 0 110 C 80 60 220 40 330 80 C 420 110 430 200 400 270 C 370 340 300 380 200 400 C 110 420 40 470 0 520 Z" fill="var(--teal-blob)" opacity="0.28"/>
    <path class="blob blob-bottom" d="M 180 600 C 220 530 330 500 420 520 C 500 540 560 580 600 600 Z" fill="var(--teal-blob)" opacity="0.25"/>
    <circle class="blob-dot" cx="686" cy="358" r="20" fill="var(--teal-soft)" opacity="0.6"/>

    <!-- accent lines -->
    <rect class="accent-bar" x="0" y="134" width="140" height="18" fill="var(--sky)"/>
    <polygon class="accent-slash" points="272,470 294,470 240,600 218,600" fill="var(--sky)"/>

    <!-- headline -->
    <g class="headline">
      <text class="headline-shadow" x="126" y="197" font-size="150" textLength="464" lengthAdjust="spacingAndGlyphs">GOOD</text>
      <text class="headline-sky" x="132" y="192" font-size="150" textLength="464" lengthAdjust="spacingAndGlyphs">GOOD</text>

      <text class="headline-shadow" x="134" y="357" font-size="200" textLength="532" lengthAdjust="spacingAndGlyphs">VIBES</text>
      <text class="headline-sun" x="140" y="352" font-size="200" textLength="532" lengthAdjust="spacingAndGlyphs">VIBES</text>

      <text class="headline-shadow" x="134" y="489" font-size="177" textLength="372" lengthAdjust="spacingAndGlyphs">ONLY</text>
      <text class="headline-sky" x="140" y="484" font-size="177" textLength="372" lengthAdjust="spacingAndGlyphs">ONLY</text>
    </g>

    <!-- shop dog badge -->
    <g class="shop-dog-badge">
      <circle class="badge-ring" cx="918" cy="252" r="142" fill="none" stroke="var(--ring-teal)" stroke-width="6"/>
      <circle class="badge-photo" cx="918" cy="240" r="130" fill="url(#dog-tones)" role="img" aria-label="Photo of the shop dog, a fluffy cream-coloured doodle, smiling"/>
      <text class="badge-caption">
        <textPath href="#caption-arc" startOffset="50%" text-anchor="middle">BEST SHOP DOG</textPath>
      </text>
    </g>

    <!-- brand -->
    <g class="brand">
      <circle class="brand-mark" cx="804" cy="462" r="38" fill="none" stroke="var(--brand-blue)" stroke-width="5"/>
      <text class="brand-name" x="854" y="474" textLength="236" lengthAdjust="spacingAndGlyphs">CORAL NOOK</text>
    </g>
    <text class="location-line" x="916" y="540" text-anchor="middle">South of bridge in Gull Harbor</text>
  </svg>
</main>
</body>
</html>
```